Promotional Poster for Music Achievement Program

I need a vertical 11x17 poster designed for a new program called Bright Steps Music Achievement Program. The poster will be displayed in the lesson rooms and lobbies of music schools who use this program. The main headline of the flyer should be "Ask your teacher about Bright Steps" And then the additional text should be "Love your lessons and practice like never before with 10 levels of achievement!" I would like to use the logo on the flyer, which I uploaded here. In terms of artwork/design, I am looking for a fun, but clean feel. The purpose of the program is for students to progress through ten levels of achievement as they climb higher and higher to mastery of their instrument at level 10, so a feel of climbing, leveling up, or advancing would be good. And of course, this is a music program, so any musical artwork involved would make sense. But again - nothing too busy or overwhelming!

Target Market(s)

Parents waiting in the lobby of a music school.

Industry/Entity Type

Promotional

Colors

Designer to choose colors to be used in the design.

Requirements
Must have
• - Bright Steps logo
• - This headline: Ask your teacher about Bright Steps
• - This additional text: Love your lessons and practice like never before with 10 levels of achievement!
Nice to have
• In terms of artwork/design, I am looking for a fun, but clean feel. The purpose of the program is for students to progress through ten levels of achievement as they climb higher and higher to mastery of their instrument at level 10, so a feel of climbing, leveling up, or advancing would be good. And of course, this is a music program, so any musical artwork involved would make sense. But again - nothing too busy or overwhelming!
Should not have
• Should not be too busy.

```html
<!DOCTYPE html>
<html lang="en">
<head>
<meta charset="utf-8">
<title>Bright Steps Music Achievement Program Poster</title>
<link rel="stylesheet" href="https://fonts.googleapis.com/css2?family=Ultra&display=swap">
<style>
  :root {
    --backdrop: #7a7979;
    --paper: #ffffff;
    --panel-grey: #cfcfd0;
    --panel-grey-light: #dcdcdd;
    --ink: #1c1c1c;
    --headline-box: #262626;
    --lime: #b5c71a;
    --orange: #f0a033;
    --red: #e3181f;
    --white: #ffffff;
    --wave-cream: #e6e2c9;
    --wave-yellow: #eeeaa8;
    --wave-stone: #cfcbb5;
    --pixel-grey: #a7a7a8;
  }
  html, body {
    margin: 0;
    padding: 0;
    width: 1200px;
    height: 900px;
    overflow: hidden;
    background: var(--backdrop);
  }
  .poster {
    position: absolute;
    left: 296px;
    top: 20px;
    width: 609px;
    height: 860px;
    background: var(--paper);
    box-shadow: 0 10px 24px rgba(0,0,0,0.35);
    font-family: "Ultra", Georgia, serif;
  }
  .content-panel {
    position: absolute;
    left: 33px;
    top: 0;
    width: 445px;
    height: 860px;
    background: linear-gradient(180deg, var(--panel-grey) 0%, var(--panel-grey-light) 60%, var(--panel-grey) 100%);
  }
  .wave-art {
    position: absolute;
    left: 478px;
    top: 0;
    width: 131px;
    height: 860px;
    background: linear-gradient(160deg, var(--paper) 0%, var(--wave-cream) 30%, var(--wave-yellow) 55%, var(--wave-stone) 75%, var(--paper) 100%);
  }
  .brand {
    position: absolute;
    left: 0;
    top: 78px;
    width: 445px;
    display: flex;
    align-items: center;
    justify-content: center;
    gap: 14px;
  }
  .brand-mark {
    width: 34px;
    height: 34px;
    background: var(--lime);
  }
  .brand-name {
    font-size: 34px;
    color: var(--ink);
    letter-spacing: 0.5px;
  }
  .headline-box {
    position: absolute;
    left: 0;
    top: 203px;
    width: 445px;
    height: 245px;
    background: var(--headline-box);
    display: flex;
    align-items: center;
    justify-content: center;
  }
  .headline {
    margin: 0;
    text-align: center;
    font-weight: 400;
    text-transform: uppercase;
    line-height: 52px;
  }
  .headline span { display: block; }
  .headline .line-ask { color: var(--lime); font-size: 46px; letter-spacing: 2px; }
  .headline .line-teacher { color: var(--orange); font-size: 50px; letter-spacing: 1px; }
  .headline .line-about { color: var(--red); font-size: 52px; letter-spacing: 2px; }
  .headline .line-name { color: var(--white); font-size: 37px; }
  .tagline {
    position: absolute;
    left: 0;
    top: 493px;
    width: 445px;
    margin: 0;
    text-align: center;
    color: var(--red);
    font-size: 20px;
    line-height: 28px;
    text-transform: uppercase;
    letter-spacing: 1px;
  }
  .pixel-art {
    position: absolute;
    left: 0;
    bottom: 0;
    width: 445px;
    height: 180px;
    background: linear-gradient(180deg, rgba(167,167,168,0) 0%, rgba(167,167,168,0.6) 45%, var(--pixel-grey) 100%);
  }
</style>
</head>
<body>
  <main class="poster">
    <section class="content-panel">
      <div class="brand">
        <span class="brand-mark"></span>
        <span class="brand-name">Bright Steps</span>
      </div>
      <div class="headline-box">
        <h1 class="headline">
          <span class="line-ask">Ask your</span>
          <span class="line-teacher">teacher</span>
          <span class="line-about">about</span>
          <span class="line-name">Bright Steps</span>
        </h1>
      </div>
      <p class="tagline">Love your lessons<br>and practice like<br>never before<br>with 10 levels of<br>achievement!</p>
      <div class="pixel-art" role="img" aria-label="Rising grey pixel equalizer bars suggesting levelling up"></div>
    </section>
    <div class="wave-art" role="img" aria-label="Flowing cream and pale yellow ribbon waves"></div>
  </main>
</body>
</html>
```